KVE Palliative Care Flyer

We need an A5 flyer designed for print on high quality card. The flyer will be placed on every seat at two Brindlewood Chamber Ensemble concerts dedicated to awareness raising of palliative care. We would like to have a flyer that uses our logo, and an image of a couple waltzing or in waltz hold. The final design should communicate the essence of palliative care which is that you matter to us, and you matter right to the very end of your life. "Putting life in the days, not days in the life".

Target Market(s)

Concert goers

Requirements
Must have
• Gentle Harbour Alliance SA logo

```html
<!DOCTYPE html>
<html lang="en">
<head>
<meta charset="utf-8">
<title>Gentle Harbour Alliance SA – Palliative Care Flyer</title>
<link href="https://fonts.googleapis.com/css2?family=Arimo:wght@400&display=swap" rel="stylesheet">
<style>
  :root {
    --paper: #ffffcc;
    --ink: #1a1a1a;
    --brand-blue: #1f95d8;
    --link-blue: #1a7fd0;
    --frame: #8c8c8c;
    --hands-light: #e6ded6;
    --hands-skin: #d9ab92;
    --stage-deep: #0a1630;
    --stage-blue: #2a4fa8;
  }
  * { box-sizing: border-box; margin: 0; padding: 0; }
  html, body { width: 900px; height: 1200px; overflow: hidden; background: var(--paper); }
  .flyer {
    position: relative; width: 900px; height: 1200px;
    background: var(--paper); color: var(--ink);
    font-family: "Arimo", Arial, sans-serif; font-size: 20.5px; line-height: 25.6px;
  }
  .copy { position: absolute; text-align: center; }
  .copy--intro { left: 0; top: 2px; width: 412px; }
  .copy--closing { left: 438px; top: 543px; width: 462px; }
  .photo { position: absolute; }
  .photo--hands {
    left: 438px; top: 52px; width: 454px; height: 443px;
    border: 1px solid var(--frame);
    background: linear-gradient(135deg, var(--hands-light) 0%, var(--hands-skin) 55%, var(--hands-light) 100%);
  }
  .photo--waltz {
    left: 16px; top: 550px; width: 379px; height: 528px;
    background: radial-gradient(ellipse at 55% 45%, var(--stage-blue) 0%, var(--stage-deep) 75%);
  }
  .contact {
    position: absolute; left: 13px; top: 1108px;
    font-size: 21px; line-height: 29px;
  }
  .contact__org { color: var(--brand-blue); }
  .contact__web { color: var(--link-blue); text-decoration: underline; }
</style>
</head>
<body>
<main class="flyer">
  <p class="copy copy--intro">
    Palliative care also seeks to be<br>
    smooth and progressive in its offer of<br>
    care&nbsp; always available, responsive,<br>
    and in partnership with the patient<br>
    and family.&nbsp; It calls for medical and<br>
    nursing expertise, but just as each<br>
    waltzing couple has its own<br>
    individual style, palliative care seeks<br>
    to be patient-centred, offering the<br>
    support that the patient and family<br>
    see as most appropriate for them.<br>
    Some persons feel they cannot<br>
    dance; many feel unable to<br>
    approach the prospect of death and<br>
    dying.<br>
    Just as everyone can learn to waltz,<br>
    everyone should be prepared to<br>
    consider the circumstances of major<br>
    illness and the treat of dying&nbsp; we<br>
    never know its timing.
  </p>

  <div class="photo photo--hands" role="img" aria-label="Photo of a young hand gently holding an elderly hand"></div>

  <div class="photo photo--waltz" role="img" aria-label="Photo of a ballroom couple in waltz hold on a blue-lit stage"></div>

  <p class="copy copy--closing">
    And we should be prepared to start a<br>
    conversation with those close to us about<br>
    how we wish a serious illness to be<br>
    managed.&nbsp; It will serve to dispel anxieties<br>
    and fears and will facilitate<br>
    communication in crisis situations.&nbsp; South<br>
    Australia is preparing Advance Care<br>
    Directives legislation that will encourage<br>
    us all to do this, and write it down.<br>
    Tonight we affirm both the spirit-lifting<br>
    rhythm of the waltz, and the heart<br>
    warming work of palliative care.<br>
    Everyone should understand also what<br>
    palliative care can offer for make the<br>
    'dance with death' something not to be<br>
    feared.&nbsp; It is not about helping to die,<br>
    more about ensuring comfort and fostering<br>
    patience, courage and love; that are the<br>
    values of life itself.&nbsp; The Gentle Harbour<br>
    Alliance will welcome your queries and<br>
    assistance.
  </p>

  <address class="contact" style="font-style: normal;">
    <span class="contact__org">Gentle Harbour Alliance South Australia</span> Inc., Suite 4a 18-22, Wattlebrook Road<br>
    Kensington SA 5068, PO Box 728, Marryatville, SA 5068<br>
    Phone: 8140 2957&nbsp; E-mail: hello@gentleharbour.org.au&nbsp; <span class="contact__web">www.gentleharbour.org.au</span>
  </address>
</main>
</body>
</html>
```